This is for a poster that will be hanging in the window of a Men's Suit Store in the mall:
Size 4 feet wide by 6 feet high
Main point is: A sale on "Suits" or "Men's Suits" at 40%-60% off ( the 40%-60% off should be the focal point)
Some words that can be used are "Sale" or "Clearance Sale"
Some key words that can be used to make it urgent are "limited time offer" or something similar.
You can get creative, the point is for the customer to want to come into the store and buy a suit right away.
You may use a graphic (picture of a man in a suit). It is not necessary but if it looks good you can use it. (If you do use a picture, it should be of a modern fit or slim fit suit)
Sorry, the initial brief somehow got deleted from the project. Please see the updated brief.
Thanks
Reason: Project was closed for some reason, extended to give enough time to complete
Target Market(s)
Mostly Men ages 35-55
Industry/Entity Type
Store
Colors
Designer to choose colors to be used in the design.

```html
<!DOCTYPE html>
<html lang="en">
<head>
<meta charset="utf-8">
<title>Men's Suits Sale Poster</title>
<link href="https://fonts.googleapis.com/css2?family=Jost:wght@300;400&family=Yellowtail&family=Italianno&family=Sorts+Mill+Goudy&display=block" rel="stylesheet">
<style>
  :root {
    --paper: #ffffff;
    --charcoal: #2a2a2a;
    --charcoal-deep: #1c1c1c;
    --navy: #0d1a3d;
    --navy-text: #1b2545;
    --cream: #ece2c8;
    --ink: #111111;
  }
  html, body {
    margin: 0;
    padding: 0;
    width: 800px;
    height: 1200px;
    overflow: hidden;
    background: var(--paper);
  }
  .poster {
    position: relative;
    width: 800px;
    height: 1200px;
    overflow: hidden;
  }
  .poster-field,
  .suit-front,
  .offer-band {
    position: absolute;
    left: 0;
    top: 0;
  }
  .suit-front {
    left: 95px;
    width: 610px;
    height: 615px;
    background: linear-gradient(90deg, #f2f2f2 0%, #d9dce4 28%, #0f1c44 50%, #d9dce4 72%, #f2f2f2 100%);
  }
  .offer-band {
    top: 300px;
    width: 800px;
    height: 160px;
    background: linear-gradient(90deg, rgba(255,255,255,0.12) 0%, rgba(255,255,255,0.45) 30%, rgba(255,255,255,0.45) 70%, rgba(255,255,255,0.12) 100%);
  }
  .brand {
    position: absolute;
    top: 66px;
    left: 0;
    width: 800px;
    text-align: center;
    color: var(--paper);
    font-family: 'Jost', sans-serif;
    font-weight: 300;
    line-height: 1;
  }
  .brand-name {
    display: block;
    font-size: 52px;
    letter-spacing: 1px;
    margin-left: -18px;
  }
  .brand-line {
    display: block;
    font-size: 29px;
    margin-top: 0;
    margin-left: -18px;
  }
  .headline {
    position: absolute;
    top: 162px;
    left: 0;
    width: 800px;
    margin: 0;
    text-align: center;
    font-family: 'Yellowtail', cursive;
    font-weight: 400;
    font-size: 122px;
    line-height: 1;
    color: var(--paper);
    -webkit-text-stroke: 10px var(--ink);
    paint-order: stroke fill;
    text-shadow: 0 0 2px var(--paper), 0 0 3px var(--paper);
    letter-spacing: 2px;
    transform: rotate(-2deg);
  }
  .discount {
    position: absolute;
    top: 326px;
    left: 0;
    width: 770px;
    margin: 0;
    text-align: center;
    font-family: 'Jost', sans-serif;
    font-weight: 300;
    font-size: 104px;
    line-height: 1;
    color: var(--navy-text);
  }
  .sale-word {
    position: absolute;
    top: 560px;
    left: 0;
    width: 800px;
    text-align: center;
    font-family: 'Italianno', cursive;
    font-size: 560px;
    line-height: 1;
    color: var(--cream);
    text-shadow: 6px 6px 14px rgba(0,0,0,0.6);
    margin-left: -10px;
  }
  .urgency {
    position: absolute;
    top: 1048px;
    left: 0;
    width: 800px;
    margin: 0;
    text-align: center;
    font-family: 'Sorts Mill Goudy', serif;
    font-size: 60px;
    line-height: 1;
    color: var(--paper);
  }
</style>
</head>
<body>
<main class="poster">
  <svg class="poster-field" width="800" height="1200" viewBox="0 0 800 1200" aria-hidden="true">
    <defs>
      <radialGradient id="field-glow" cx="0.5" cy="0.45" r="0.7">
        <stop offset="0" stop-color="#333333"/>
        <stop offset="1" stop-color="#1e1e1e"/>
      </radialGradient>
    </defs>
    <polygon points="0,0 780,0 800,14 800,1138 0,1176" fill="url(#field-glow)"/>
  </svg>

  <div class="suit-front" role="img" aria-label="Illustration of a suit jacket's white lapels forming a V around a navy shirt front"></div>
  <div class="offer-band" aria-hidden="true"></div>

  <div class="brand">
    <span class="brand-name">hartwell</span>
    <span class="brand-line">menswear</span>
  </div>

  <h1 class="headline">Men's Suits</h1>
  <p class="discount">40%-60% off</p>
  <div class="sale-word">Sale</div>
  <p class="urgency">limited time offer</p>
</main>
</body>
</html>
```